Tandrew Advisory Group Business Card Design Project

2-sided business card for my small (me and a couple subcontractors) firm, which consults to public community colleges and school districts and public agencies in California on energy matters, mostly solar electric systems that can reduce their electricity use by as much as 80%. I prepare requests for proposals (RFPs), manage the RFP processes, and work with the solar vendors to get the best deal for my clients. I also do regulatory and legislative advocacy for strong renewable energy policies. I do lots of quantitative analysis to make sure the solar systems are sized to produce the maximum monetary savings and focus a lot on the aesthetic design of the solar systems, as architectural features of the campuses (most are carport structures built in parking lots, but some are built on the ground and on rooftops). All my work is geared to getting the best value, highest quality, and most reliable solar system. My career background is in public interest energy advocacy; I'm not a consultant trying to make a million dollars but someone who is still serving in the public interest.

My competition is made up of much larger firms; this business card/logo in large part is intended to present an image of my firm as an equal to these larger firms despite my smaller size.

Essential information as follows:
Firm name: Tandrew Advisory Group
Tagline: Clean Energy Procurement for the Public Sector
Name: Gavin Tandrew
email, 2 phone number, and address listed as well.

Target Market(s)

Public schools, community colleges, & public agencies.There is a wide range in the sophistication of these organizations.

Industry/Entity Type

Parking

Requirements
Must have
• - several rich colors, which can be either in the logo or in the background - the overall feeling of the card should reflect richness of color. I have uploaded some photos showing some colors that I like together. By rich I do not necessarily mean bright. I suppose bright colors in the logo could be supported with rich colors in the overall background of the card.
- professional, and powerful in an understated way (not kooky, cartoonish, or very playful)
- the logo must NOT be too representational of solar energy or the sun, but at the same time it would be good for the logo to be somewhat suggestive of this.

Nice to have
• -I like abstract and geometric images (with rich colts).
- A very subtle reference to schools/colleges/education would be great but it CANNOT be explicit; it would have to be faintly suggestive.
- In the logo I like the idea of abstract or geometric shapes intersecting with other in an interesting and suggestive way, conveying the multiple aspects of my practice (economics, data analysis, energy analysis, problem solving, managing collaborative processes, policy analysis)
- My work relates to environmental concerns, especially climate change. Working this into the logo in a subtle way could be good, but it's not a requirement.
- I like the idea that the logo/card feels serene.
- In designing the business card, I kind of like the idea of having the tag line as the first thing they read, then they see the firm name.

Should not have
• Not:
- humorous
- boring
- overly slick
- overly formal
- whimsical

```html
<!DOCTYPE html>
<html lang="en">
<head>
<meta charset="utf-8">
<title>Tandrew Advisory Group — Business Card</title>
<link rel="stylesheet" href="https://fonts.googleapis.com/css2?family=Oswald:wght@500;600&family=Open+Sans:wght@400;600&display=swap">
<style>
  :root {
    --plum: #622a6e;
    --lilac: #b07cb8;
    --lilac-soft: #a57ab0;
    --white: #ffffff;
    --ink: #111111;
    --stage-light: #ffffff;
    --stage-edge: #b1b2b4;
  }
  * { box-sizing: border-box; margin: 0; padding: 0; }
  html, body { width: 1200px; height: 1000px; overflow: hidden; }
  body {
    position: relative;
    background: radial-gradient(ellipse 62% 60% at 50% 50%, var(--stage-light) 0%, #ececed 45%, var(--stage-edge) 100%);
    font-family: "Open Sans", Arial, sans-serif;
  }

  .card {
    position: absolute;
    width: 510px;
    height: 306px;
    background: var(--plum);
    overflow: hidden;
    color: var(--white);
  }

  /* Front */
  .card-front { left: 190px; top: 161px; }
  .corner-mark { position: absolute; left: 0; top: 0; }
  .firm-name {
    position: absolute;
    left: 60px; top: 60px;
    width: 430px; height: 180px;
    display: flex; align-items: center; justify-content: center; gap: 22px;
  }
  .firm-dot {
    width: 46px; height: 46px; border-radius: 50%;
    background: var(--white); flex: none;
  }
  .firm-wordmark {
    font-family: "Oswald", "Arial Narrow", sans-serif;
    font-weight: 600;
    color: var(--white);
    text-transform: uppercase;
    line-height: 1;
  }
  .firm-wordmark .line-main { display: block; font-size: 74px; letter-spacing: 1px; }
  .firm-wordmark .line-sub { display: block; font-size: 33px; letter-spacing: 2px; margin-top: 8px; }
  .tagline {
    position: absolute;
    left: 0; right: 0; top: 274px;
    text-align: center;
    font-size: 16.5px; font-weight: 600;
    letter-spacing: 0.1px;
  }

  /* Rear */
  .card-rear { left: 540px; top: 524px; }
  .band { position: absolute; left: 0; width: 100%; background: var(--lilac); }
  .band-top { top: 0; height: 26px; }
  .band-bottom { bottom: 0; height: 30px; }
  .holder-name {
    position: absolute;
    left: 14px; top: 52px;
    width: 262px;
    font-family: "Oswald", "Arial Narrow", sans-serif;
    font-weight: 600;
    text-transform: uppercase;
    line-height: 0.98;
    color: var(--white);
  }
  .holder-name .given { display: block; font-size: 84px; letter-spacing: 1px; }
  .holder-name .family { display: block; font-size: 66px; letter-spacing: 0; margin-top: 4px; }

  .contact-list { position: absolute; left: 292px; top: 48px; list-style: none; }
  .contact-item {
    position: absolute; left: 0;
    display: flex; align-items: center; gap: 8px;
    font-size: 14.5px; white-space: nowrap;
  }
  .contact-item svg { flex: none; }
  .contact-email { top: 0; font-size: 13.5px; }
  .contact-phone-1 { top: 34px; }
  .contact-phone-2 { top: 90px; }
  .contact-address { top: 138px; }
  .contact-address span { margin-left: 4px; }

  /* Presentation labels */
  .side-label {
    position: absolute;
    display: flex; align-items: center; gap: 12px;
    font-family: "Open Sans", Arial, sans-serif;
    font-size: 60px; color: var(--ink);
    line-height: 1;
  }
  .label-front { left: 762px; top: 268px; }
  .label-rear { left: 258px; top: 643px; }
</style>
</head>
<body>

  <section class="card card-front" aria-label="Business card front">
    <svg class="corner-mark" width="130" height="130" viewBox="0 0 130 130" aria-hidden="true">
      <polygon points="0,0 128,0 0,128" fill="var(--white)"/>
      <polygon points="12,10 104,10 12,102" fill="var(--lilac-soft)"/>
      <polygon points="20,10 104,10 20,94" fill="var(--plum)"/>
    </svg>
    <div class="firm-name">
      <span class="firm-dot" aria-hidden="true"></span>
      <h1 class="firm-wordmark">
        <span class="line-main">Tandrew</span>
        <span class="line-sub">Advisory Group</span>
      </h1>
    </div>
    <p class="tagline">Clean Energy Procurement for the Public Sector</p>
  </section>

  <section class="card card-rear" aria-label="Business card back">
    <div class="band band-top"></div>
    <div class="band band-bottom"></div>
    <h2 class="holder-name">
      <span class="given">Gavin</span>
      <span class="family">Tandrew</span>
    </h2>
    <ul class="contact-list">
      <li class="contact-item contact-email">
        <svg width="16" height="16" viewBox="0 0 16 16" aria-hidden="true">
          <circle cx="8" cy="8" r="3" fill="none" stroke="var(--white)" stroke-width="1.8"/>
          <path d="M11 5v4.5c0 1.5 2.8 1.5 2.8-1.5A5.8 5.8 0 1 0 10.5 13" fill="none" stroke="var(--white)" stroke-width="1.8"/>
        </svg>
        gavintandrew@mailbox.org
      </li>
      <li class="contact-item contact-phone-1">
        <svg width="12" height="34" viewBox="0 0 12 34" aria-hidden="true">
          <circle cx="6" cy="5" r="4" fill="none" stroke="var(--white)" stroke-width="1.8"/>
          <rect x="4" y="11" width="4" height="12" fill="var(--white)"/>
          <circle cx="6" cy="29" r="4" fill="none" stroke="var(--white)" stroke-width="1.8"/>
        </svg>
        000-000-0000000
      </li>
      <li class="contact-item contact-phone-2">
        <svg width="12" height="34" viewBox="0 0 12 34" aria-hidden="true">
          <circle cx="6" cy="5" r="4" fill="none" stroke="var(--white)" stroke-width="1.8"/>
          <rect x="4" y="11" width="4" height="12" fill="var(--white)"/>
          <circle cx="6" cy="29" r="4" fill="none" stroke="var(--white)" stroke-width="1.8"/>
        </svg>
        000-000-0000000
      </li>
      <li class="contact-item contact-address">
        <svg width="22" height="14" viewBox="0 0 22 14" aria-hidden="true">
          <rect x="0" y="0" width="22" height="14" fill="var(--white)"/>
          <path d="M0 0 L11 8 L22 0" fill="none" stroke="var(--plum)" stroke-width="1.6"/>
        </svg>
        <span>Address</span>
      </li>
    </ul>
  </section>

  <div class="side-label label-front">
    <svg width="88" height="84" viewBox="0 0 88 84" aria-hidden="true">
      <polygon points="0,42 86,0 58,42 86,84" fill="var(--ink)"/>
    </svg>
    <span>Front</span>
  </div>

  <div class="side-label label-rear">
    <span>Rear</span>
    <svg width="88" height="84" viewBox="0 0 88 84" aria-hidden="true">
      <polygon points="88,42 2,0 30,42 2,84" fill="var(--ink)"/>
    </svg>
  </div>

</body>
</html>
```